Stationary for a computer tech, hardware selling & website building & hosting for smb's
Pavillon Informatique
Professional
Mathieu Ostrowel
Directeur associé
4187 Boul. Lanvoisier Est
Montréal (Qc) H7T 8W2
514.555.0148 p.317
mathieu@pavillon-exemple.ca
www.pavillon-exemple.ca
Logo on white background
Logo on black background

```html
<!DOCTYPE html>
<html lang="fr">
<head>
<meta charset="utf-8">
<title>Pavillon Informatique – Papeterie</title>
<link href="https://fonts.googleapis.com/css2?family=Arimo:wght@400;700&display=swap" rel="stylesheet">
<style>
  :root {
    --frame: #1e1e1e;
    --board: #a9a9a9;
    --green: #7cc12f;
    --charcoal: #484848;
    --white: #ffffff;
    --ink: #333333;
    --rule: #3a3a3a;
  }
  * { margin: 0; padding: 0; box-sizing: border-box; }
  html, body { width: 1200px; height: 715px; overflow: hidden; background: var(--frame); }
  body { font-family: "Arimo", Arial, sans-serif; }
  .board {
    position: absolute; left: 14px; top: 14px; width: 1172px; height: 687px;
    background: var(--board);
  }
  .card {
    position: absolute; width: 510px; height: 287px; border-radius: 22px;
    overflow: hidden; border: 1px solid #6c6c6c;
  }
  .card--front { left: 56px; top: 41px; background: var(--white); }
  .card--green { left: 593px; top: 41px; background: var(--green); }
  .card--white { left: 56px; top: 353px; background: var(--white); }
  .card--dark  { left: 593px; top: 353px; background: var(--charcoal); }

  .brand { position: absolute; display: flex; align-items: center; gap: 12px; }
  .brand__dot { border-radius: 50%; flex: none; }
  .brand__name { font-weight: 700; white-space: nowrap; }

  .card--front .brand { left: 20px; top: 18px; }
  .card--front .brand__dot { width: 60px; height: 60px; background: var(--charcoal); }
  .card--front .brand__name { font-size: 30px; color: var(--green); letter-spacing: -0.5px; }

  .holder { position: absolute; left: 0; right: 0; top: 122px; text-align: center; padding-left: 120px; }
  .holder__name { font-size: 22px; font-weight: 700; color: var(--green); }
  .holder__role { font-size: 14px; color: var(--ink); margin-top: 3px; }

  .swoosh { position: absolute; left: 0; top: 0; width: 510px; height: 287px; }
  .contact {
    position: absolute; left: 0; right: 0; top: 192px; text-align: center;
    padding-left: 120px; color: var(--white); font-size: 12.5px; line-height: 17px;
  }

  .mark { left: 50%; top: 50%; transform: translate(-50%, -50%); flex-direction: column; gap: 16px; }
  .mark .brand__dot { width: 96px; height: 96px; }
  .mark .brand__name { font-size: 28px; }
  .card--green .brand__dot { background: var(--white); }
  .card--green .brand__name { color: var(--white); }
  .card--white .brand__dot { background: var(--green); }
  .card--white .brand__name { color: var(--charcoal); }
  .card--dark .brand__dot { background: var(--white); }
  .card--dark .brand__name { color: var(--white); }
</style>
</head>
<body>
<main class="board">
  <section class="card card--front">
    <div class="brand">
      <span class="brand__dot"></span>
      <span class="brand__name">Pavillon Informatique</span>
    </div>
    <div class="holder">
      <p class="holder__name">Mathieu Ostrowel</p>
      <p class="holder__role">Directeur associé</p>
    </div>
    <svg class="swoosh" viewBox="0 0 510 287" aria-hidden="true">
      <path d="M0 196 Q255 148 510 196 L510 287 L0 287 Z" fill="var(--green)"/>
      <path d="M0 190 Q255 140 510 190" fill="none" stroke="var(--rule)" stroke-width="3"/>
    </svg>
    <div class="contact">
      <p>4187 Boul. Lanvoisier Est, Montréal (Qc) H7T 8W2</p>
      <p>Cell: 514.555.0192 | Phone: 514.555.0148 p.317</p>
      <p>Fax: 514.555.0163</p>
      <p>Email: mathieu@pavillon-exemple.ca | www.pavillon-exemple.ca</p>
    </div>
  </section>

  <section class="card card--green">
    <div class="brand mark">
      <span class="brand__dot"></span>
      <span class="brand__name">Pavillon Informatique</span>
    </div>
  </section>

  <section class="card card--white">
    <div class="brand mark">
      <span class="brand__dot"></span>
      <span class="brand__name">Pavillon Informatique</span>
    </div>
  </section>

  <section class="card card--dark">
    <div class="brand mark">
      <span class="brand__dot"></span>
      <span class="brand__name">Pavillon Informatique</span>
    </div>
  </section>
</main>
</body>
</html>
```